National hospice pharmacy network needs business cards

We need a business cards for a new company that is creating a network of independent pharmacies to provide medication delivery to hospice patients in their area. We will be providing them with logistics to build a delivery system, software to increase efficiency and the marketing to hospice agencies. The pharmacies will benefit with increasing their patient care, increasing their efficiency and increasing their profits.

the logo design is approved we are just darkening the colors. The logo will be updated when we have the final approval

Marketing

```html
<!DOCTYPE html>
<html lang="en">
<head>
<meta charset="utf-8">
<title>MedRelay Business Card</title>
<link rel="stylesheet" href="https://fonts.googleapis.com/css2?family=Arimo:wght@400;700&family=Tinos:ital,wght@0,400;0,700;1,400;1,700&display=swap">
<style>
  :root {
    --brand-blue: #2b5ca6;
    --band-blue: #243e8d;
    --text-blue: #2a3f91;
    --brand-green: #3fae49;
    --ink: #111111;
    --paper: #ffffff;
  }
  html, body {
    margin: 0;
    padding: 0;
    overflow: hidden;
    background: var(--paper);
  }
  .card {
    position: relative;
    width: 1200px;
    height: 686px;
    background: var(--paper);
    overflow: hidden;
  }
  .card-shapes {
    position: absolute;
    inset: 0;
  }
  .shape-green { fill: var(--brand-green); }
  .shape-blue { fill: var(--band-blue); }

  .brand {
    position: absolute;
    left: 46px;
    top: 70px;
    display: flex;
    align-items: center;
    gap: 22px;
  }
  .brand-name {
    margin: 0;
    font-family: "Arimo", Arial, sans-serif;
    font-weight: 700;
    font-size: 128px;
    line-height: 1;
    letter-spacing: -3px;
    color: var(--brand-blue);
  }
  .brand-dot {
    width: 40px;
    height: 40px;
    border-radius: 50%;
    background: var(--brand-green);
    margin-top: 30px;
  }

  .benefits {
    position: absolute;
    left: 746px;
    top: 72px;
    margin: 0;
    font-family: "Tinos", "Times New Roman", serif;
    font-style: italic;
    font-size: 39px;
    line-height: 49px;
    color: var(--ink);
  }

  .mission {
    position: absolute;
    left: 40px;
    top: 307px;
    margin: 0;
    width: 640px;
    font-family: "Tinos", "Times New Roman", serif;
    font-style: italic;
    font-weight: 700;
    font-size: 37px;
    line-height: 51px;
    color: var(--text-blue);
  }

  .services {
    position: absolute;
    left: 747px;
    top: 278px;
    margin: 0;
    padding: 0;
    list-style: none;
    font-family: "Arimo", Arial, sans-serif;
    font-size: 41px;
    line-height: 70px;
    color: var(--paper);
  }

  .contact {
    position: absolute;
    left: 46px;
    top: 543px;
    color: var(--paper);
    font-family: "Tinos", "Times New Roman", serif;
  }
  .contact-name {
    margin: 0;
    font-weight: 700;
    font-size: 35px;
    line-height: 44px;
  }
  .contact-details {
    margin: 4px 0 0;
    font-size: 37px;
    line-height: 46px;
    white-space: nowrap;
  }
</style>
</head>
<body>
  <main class="card">
    <svg class="card-shapes" width="1200" height="686" viewBox="0 0 1200 686" aria-hidden="true">
      <path class="shape-green" d="M711,330 Q711,225 830,225 L1200,225 L1200,520 L711,531 Z"/>
      <path class="shape-blue" d="M0,511 L711,511 L711,532 Q735,497 830,497 L1200,497 L1200,686 L0,686 Z"/>
    </svg>

    <div class="brand">
      <h1 class="brand-name">MedRelay</h1>
      <span class="brand-dot"></span>
    </div>

    <p class="benefits">Increase patient care,<br>efficiency and profits</p>

    <p class="mission">Creating a network of independent pharmacies to provide medication delivery to hospice patients</p>

    <ul class="services">
      <li>Delivery System</li>
      <li>Software</li>
      <li>Marketing</li>
    </ul>

    <div class="contact">
      <p class="contact-name">Name of Agent</p>
      <p class="contact-details">Address Address Address • www.medrelay.com • 000-000-0000</p>
    </div>
  </main>
</body>
</html>
```